New website for Holloway Law Firm at www.keepfirmplan.example

We are a professional law firm located in the Nashville, Tennessee USA area. We focus on personal injury law. We are looking for a slick new website that is user friendly for updating with new blogs, videos, etc. The primary colors should be red, black, and white. It should load extremely fast and have a good mobile component. The pages for the design will include a home page, about us, news, contact us, and practice page. The practice page will be copied for all the practice areas including motor vehicle accidents, slip and fall accidents, dog bites, etc. We have included an image which we would like to include in the new site which shows the color scheme The image is called banner-Car Wreck. The new website should NOT have gavels, court houses, law books, scales or the typical images for a law firm.

Target Market(s)

People in Tennessee involved in accidents

Industry/Entity Type

Legal services, law firm

Number of Pages Required

5+ page

Font styles to use
Serif

Colors
EB3D1F
EC4F4E
F09395
F8D3D4
FCEDEE

Requirements
Should not have
• Gavels, columns, scales, law related images

```html
<!DOCTYPE html>
<html lang="en">
<head>
<meta charset="utf-8">
<title>Holloway Law Firm</title>
<link href="https://fonts.googleapis.com/css2?family=Open+Sans:wght@400;600;700;800&display=swap" rel="stylesheet">
<style>
:root{
  --red:#e8141b;
  --black:#000;
  --dark:#1c1c1c;
  --white:#fff;
  --grey:#ebebeb;
  --text:#222;
  --muted:#555;
}
*{margin:0;padding:0;box-sizing:border-box}
html,body{width:1200px;height:3007px;overflow:hidden}
body{position:relative;font-family:"Open Sans",Arial,sans-serif;color:var(--text);background:var(--white)}
.abs{position:absolute}
a{color:inherit;text-decoration:none}

/* header */
.site-header{left:0;top:0;width:1200px;height:80px;background:var(--white)}
.brand{left:88px;top:20px;font-size:30px;font-weight:800;color:var(--red);letter-spacing:.2px}
.nav{top:30px;font-size:15px;color:#333}
.nav.active{color:var(--red);font-weight:600;border-bottom:1px solid var(--red)}
.phone-chip{left:836px;top:25px;width:30px;height:30px;border-radius:50%;background:#eee;display:flex;align-items:center;justify-content:center}
.phone-num{left:870px;top:29px;font-size:15px;font-weight:600;color:#222}
.btn-red{background:var(--red);color:var(--white);font-weight:700;display:flex;align-items:center;justify-content:center;border-radius:2px}
.header-cta{left:1012px;top:23px;width:99px;height:32px;font-size:13px}

/* hero */
.hero{left:0;top:80px;width:1200px;height:463px;background:var(--black)}
.hero-photo{left:513px;top:80px;width:687px;height:463px;background:radial-gradient(ellipse at 60% 55%,#d21a1e 0%,#8e0f12 35%,#2a0606 70%,#000 100%)}
.hero-rule{left:0;top:543px;width:1200px;height:4px;background:var(--red)}
.hero-kicker{left:88px;top:220px;font-size:19px;font-weight:600;color:var(--white)}
.hero-title{left:88px;top:252px;font-size:35px;line-height:41px;font-weight:700;color:var(--white)}
.hero-cta{left:88px;top:364px;width:182px;height:36px;font-size:13.5px}
.hero-caption{left:705px;top:435px;font-size:13px;color:#eee}
.dot{width:14px;height:14px;border-radius:2px;background:#b01014}
.dot.on{background:var(--white)}

/* about */
.about-frame{left:88px;top:675px;width:431px;height:361px;background:var(--red)}
.about-photo{left:104px;top:627px;width:432px;height:393px;background:linear-gradient(135deg,#3a2a22 0%,#7a4c33 45%,#d9d2c8 70%,#5a3a28 100%)}
.h2{font-size:37px;font-weight:700;color:var(--red)}
.about-title{left:616px;top:677px}
.about-lead{left:616px;top:750px;width:470px;font-size:15px;font-weight:700;line-height:20px;color:#111}
.about-copy{left:616px;width:475px;font-size:13px;line-height:18px;color:#444}
.btn-outline{border:1px solid #333;border-radius:2px;display:flex;align-items:center;justify-content:center;font-size:13px;font-weight:600;color:#222;background:var(--white)}
.about-more{left:616px;top:949px;width:115px;height:35px}

/* practice */
.practice-band{left:0;top:1117px;width:1200px;height:363px;background:var(--black)}
.practice-grey{left:0;top:1480px;width:1200px;height:205px;background:var(--grey)}
.practice-title{left:0;top:1186px;width:1200px;text-align:center}
.area-photo{width:232px;height:200px;top:1280px}
.area-label{top:1440px;width:188px;height:80px;background:var(--white);box-shadow:2px 3px 4px rgba(0,0,0,.15);display:flex;align-items:center;padding-left:39px;font-size:16.5px;font-weight:600;line-height:19px;color:#222}
.area-label.active{background:var(--red);color:var(--white);left:396px}
.slider-arrow{top:1428px}
.view-all{left:525px;top:1572px;width:148px;height:34px}

/* news */
.news-title{left:0;top:1755px;width:1200px;text-align:center}
.news-card{top:1832px;width:325px;height:329px;background:var(--white);box-shadow:0 0 6px rgba(0,0,0,.12)}
.news-photo{position:absolute;left:9px;top:8px;width:308px;height:180px}
.news-day{position:absolute;left:20px;top:213px;font-size:29px;font-weight:700;color:var(--red)}
.news-month{position:absolute;left:17px;top:252px;font-size:11px;color:#333}
.news-text{position:absolute;left:88px;top:218px;width:225px;font-size:15px;line-height:18px;color:#222}
.news-more{position:absolute;left:88px;top:284px;font-size:13px;font-weight:600;color:#222;display:flex;align-items:center;gap:12px}
.news-more.active{color:var(--red)}

/* consultation */
.consult{left:0;top:2243px;width:1200px;height:454px;background:linear-gradient(90deg,#cfcfcf 0%,#e9e9e9 25%,#f0f0f0 50%,#e6e6e6 75%,#bdbdbd 100%)}
.consult-title{left:0;top:2314px;width:1200px;text-align:center}
.field{background:var(--white);font-size:10px;color:#999;padding:12px 15px}
.submit{left:552px;top:2583px;width:96px;height:34px;font-size:14px}

/* footer */
.footer{left:0;top:2697px;width:1200px;height:267px;background:var(--dark)}
.foot-h{top:2748px;font-size:18px;font-weight:600;color:var(--red)}
.foot-list{top:2784px;font-size:13px;line-height:26.3px;color:var(--white);list-style:none}
.foot-list .current{color:var(--red);text-decoration:underline}
.contact-row{left:517px;font-size:13px;line-height:20px;color:var(--white);display:flex;gap:14px}
.map{left:801px;top:2753px;width:310px;height:159px;background:linear-gradient(135deg,#eef1f3,#dfe6ea);border:2px solid var(--white)}
.bottom-bar{left:0;top:2964px;width:1200px;height:43px;background:var(--red)}
.copyright{left:88px;top:2976px;font-size:13px;color:var(--white)}
.social{top:2980px;width:11px;height:11px;border-radius:50%;background:var(--white)}
</style>
</head>
<body>

<header class="abs site-header">
  <div class="abs brand">Holloway Law Firm</div>
  <a class="abs nav active" style="left:465px">Home</a>
  <a class="abs nav" style="left:541px">About Us</a>
  <a class="abs nav" style="left:636px">Practice Areas</a>
  <a class="abs nav" style="left:765px">News</a>
  <div class="abs phone-chip"><svg width="14" height="14" viewBox="0 0 24 24"><path fill="#e8141b" d="M6.6 10.8a15.1 15.1 0 006.6 6.6l2.2-2.2c.3-.3.7-.4 1-.2 1.1.4 2.3.6 3.6.6.6 0 1 .4 1 1V20c0 .6-.4 1-1 1A17 17 0 013 4c0-.6.4-1 1-1h3.5c.6 0 1 .4 1 1 0 1.3.2 2.5.6 3.6.1.3 0 .7-.2 1z"/></svg></div>
  <div class="abs phone-num">(615) 555-0142</div>
  <a class="abs btn-red header-cta">Contact Us</a>
</header>

<section>
  <div class="abs hero"></div>
  <div class="abs hero-photo" role="img" aria-label="Red car crashing with shattering glass"></div>
  <div class="abs hero-rule"></div>
  <p class="abs hero-kicker">We Make Difference</p>
  <h1 class="abs hero-title">Our Firm Offers a Wide<br>Range of Legal Services</h1>
  <a class="abs btn-red hero-cta">Book an Appointment</a>
  <span class="abs hero-caption">Lorem Ipsum</span>
  <span class="abs dot" style="left:1060px;top:495px"></span>
  <span class="abs dot" style="left:1078px;top:495px"></span>
  <span class="abs dot on" style="left:1060px;top:512px"></span>
  <span class="abs dot" style="left:1078px;top:512px"></span>
</section>

<section>
  <div class="abs about-frame"></div>
  <div class="abs about-photo" role="img" aria-label="Hands reviewing and signing documents at a desk"></div>
  <h2 class="abs h2 about-title">About Us</h2>
  <p class="abs about-lead">Lorem Ipsum is simply dummy text of the printing and typesetting industry.</p>
  <p class="abs about-copy" style="top:807px">Lorem Ipsum has been the industry's standard dummy text ever since the 1500s, when an unknown printer took a galley of type and scrambled it to make a type specimen book.</p>
  <p class="abs about-copy" style="top:877px">It has survived not only five centuries, but also the leap into electronic typeset-ting, remaining essentially unchanged.</p>
  <a class="abs btn-outline about-more">Read More</a>
</section>

<section>
  <div class="abs practice-band"></div>
  <div class="abs practice-grey"></div>
  <h2 class="abs h2 practice-title">Practice Areas</h2>

  <div class="abs area-photo" style="left:88px;background:linear-gradient(135deg,#2b3b5c,#8b9099 60%,#d5d5d5)" role="img" aria-label="Two cars after a collision"></div>
  <div class="abs area-photo" style="left:351px;background:linear-gradient(135deg,#d8d8d8,#c9a235 50%,#3a3a3a)" role="img" aria-label="Worker slipping beside a wet floor sign"></div>
  <div class="abs area-photo" style="left:615px;background:linear-gradient(135deg,#4a3a2a,#b07a3e 45%,#4c5a6e)" role="img" aria-label="Dog biting an arm"></div>
  <div class="abs area-photo" style="left:880px;background:linear-gradient(135deg,#cfd3d8,#8a6a4a 55%,#2a2a2a)" role="img" aria-label="Business meeting at a table"></div>

  <div class="abs area-label" style="left:132px">Motor Vehicle<br>Accidents</div>
  <div class="abs area-label active">Slip and Fall<br>Accidents</div>
  <div class="abs area-label" style="left:660px">Dog Bites</div>
  <div class="abs area-label" style="left:924px">Business Law</div>

  <svg class="abs slider-arrow" style="left:36px" width="16" height="24" viewBox="0 0 16 24"><path d="M12 2L3 12l9 10" fill="none" stroke="#fff" stroke-width="2"/></svg>
  <svg class="abs slider-arrow" style="left:1146px" width="16" height="24" viewBox="0 0 16 24"><path d="M4 2l9 10-9 10" fill="none" stroke="#fff" stroke-width="2"/></svg>

  <a class="abs btn-outline view-all">View All Practice</a>
</section>

<section>
  <h2 class="abs h2 news-title">News</h2>

  <article class="abs news-card" style="left:88px">
    <div class="news-photo" style="background:linear-gradient(135deg,#9aa6b0,#d9d9d9 50%,#5b6470)" role="img" aria-label="Woman helping an injured cyclist near a car"></div>
    <div class="news-day">26</div><div class="news-month">Nov, 21</div>
    <p class="news-text">Lorem Ipsum is simply dummy teaxt of the printing and type-setting industry.</p>
    <a class="news-more">Read More <svg width="8" height="10" viewBox="0 0 8 10"><path d="M2 1l4 4-4 4" fill="none" stroke="#222" stroke-width="1.6"/></svg></a>
  </article>

  <article class="abs news-card" style="left:436px">
    <div class="news-photo" style="background:linear-gradient(135deg,#3a2e28,#a88a70 50%,#d0d0d0)" role="img" aria-label="Small dog biting a hand"></div>
    <div class="news-day">26</div><div class="news-month">Nov, 21</div>
    <p class="news-text">Lorem Ipsum is simply dummy teaxt of the printing and type-setting industry.</p>
    <a class="news-more active">Read More <svg width="22" height="22" viewBox="0 0 22 22"><circle cx="11" cy="11" r="11" fill="#e8141b"/><path d="M9 6l5 5-5 5" fill="none" stroke="#fff" stroke-width="2"/></svg></a>
  </article>

  <article class="abs news-card" style="left:785px">
    <div class="news-photo" style="background:linear-gradient(135deg,#cfcfcf,#a8a39a 50%,#6a6f78)" role="img" aria-label="Person fallen on a wet office floor beside a caution sign"></div>
    <div class="news-day">26</div><div class="news-month">Nov, 21</div>
    <p class="news-text">Lorem Ipsum is simply dummy teaxt of the printing and type-setting industry.</p>
    <a class="news-more">Read More <svg width="8" height="10" viewBox="0 0 8 10"><path d="M2 1l4 4-4 4" fill="none" stroke="#222" stroke-width="1.6"/></svg></a>
  </article>
</section>

<section>
  <div class="abs consult" role="img" aria-label="Faded black and white photo of people in a consultation"></div>
  <h2 class="abs h2 consult-title">Book Free Consultation</h2>
  <div class="abs field" style="left:228px;top:2390px;width:362px;height:37px">Full Name</div>
  <div class="abs field" style="left:228px;top:2441px;width:362px;height:40px">Email*</div>
  <div class="abs field" style="left:228px;top:2495px;width:362px;height:41px">Phone</div>
  <div class="abs field" style="left:608px;top:2390px;width:363px;height:146px">Have questions? We have answers!*</div>
  <a class="abs btn-red submit">Submit</a>
</section>

<footer>
  <div class="abs footer"></div>
  <h3 class="abs foot-h" style="left:88px">Quick Link</h3>
  <ul class="abs foot-list" style="left:88px">
    <li class="current">Home</li><li>About Us</li><li>Practice Areas</li><li>News</li><li>Contact Us</li>
  </ul>
  <h3 class="abs foot-h" style="left:279px">Practice Areas</h3>
  <ul class="abs foot-list" style="left:279px">
    <li>Motor Vehicle Accidents</li><li>Slip and Fall Accidents</li><li>Dog Bites</li><li>Business Law</li><li>View All Practice</li>
  </ul>
  <h3 class="abs foot-h" style="left:517px">Conatct info</h3>
  <div class="abs contact-row" style="top:2786px">
    <svg width="15" height="18" viewBox="0 0 15 18"><path d="M7.5 0A7 7 0 000.5 7c0 5 7 11 7 11s7-6 7-11a7 7 0 00-7-7zm0 10a3 3 0 110-6 3 3 0 010 6z" fill="#e8141b"/></svg>
    <span>lorem ipsum, 354 Harbor Street<br>Nashville, TN 37201</span>
  </div>
  <div class="abs contact-row" style="top:2848px">
    <svg width="15" height="15" viewBox="0 0 24 24"><path fill="#e8141b" d="M6.6 10.8a15.1 15.1 0 006.6 6.6l2.2-2.2c.3-.3.7-.4 1-.2 1.1.4 2.3.6 3.6.6.6 0 1 .4 1 1V20c0 .6-.4 1-1 1A17 17 0 013 4c0-.6.4-1 1-1h3.5c.6 0 1 .4 1 1 0 1.3.2 2.5.6 3.6.1.3 0 .7-.2 1z"/></svg>
    <span>(615) 555-0142</span>
  </div>
  <div class="abs contact-row" style="top:2891px">
    <svg width="15" height="12" viewBox="0 0 15 12"><rect width="15" height="12" rx="1" fill="#e8141b"/><path d="M1 1l6.5 5L14 1" fill="none" stroke="#1c1c1c" stroke-width="1.3"/></svg>
    <span>info@keepfirmplan.example</span>
  </div>
  <div class="abs map" role="img" aria-label="Street map showing the office location"></div>
  <div class="abs bottom-bar"></div>
  <p class="abs copyright">Copyright © 2021 Holloway Law Firm. All Rights Reserved</p>
  <span class="abs social" style="left:1005px"></span>
  <span class="abs social" style="left:1034px"></span>
  <span class="abs social" style="left:1066px"></span>
  <span class="abs social" style="left:1098px"></span>
</footer>

</body>
</html>
```